KELPMARROW, LLC needs a hybrid app to evaluate and develop athletes

KELPMARROW, LLC needs initial hybrid mobile app and website holding page. KELPMARROW, LLC allows athletes to develop their skills (soccer is initial sport) for free. Receive daily/weekly reminders. Access training videos. Earn points to "upgrade" their soccer profile in "app soccer store". See their points/rankings compared to all app users. Progress streak. This free app (for athletes) will communicate to paid app (coaches) in the future. We would like to see designs use the color blue. The design will communicate health and wellness.

```html
<!DOCTYPE html>
<html lang="en">
<head>
<meta charset="utf-8">
<title>KELPMARROW – Athlete App Screens</title>
<link rel="stylesheet" href="https://fonts.googleapis.com/css2?family=Titillium+Web:wght@600;700&family=IBM+Plex+Sans:wght@400;600&display=swap">
<style>
:root{
  --page:#eef2f8;
  --blue-deep:#143a86;
  --blue-mid:#2350a8;
  --blue-soft:#3a67bd;
  --bar:#0c3a93;
  --navy:#0f1535;
  --white:#ffffff;
  --nav-chip:#d7deec;
  --ink:#1b2340;
  --grey-ball:#5b5f66;
  --ok:#22b24c;
  --no:#e5202e;
}
*{margin:0;padding:0;box-sizing:border-box}
html,body{width:1200px;height:661px;overflow:hidden;background:var(--page)}
body{position:relative;font-family:"IBM Plex Sans",sans-serif;color:var(--white)}
.screen{position:absolute;top:106px;width:212px;height:458px;border-radius:22px;overflow:hidden;
  background:linear-gradient(180deg,var(--blue-mid) 0%,var(--blue-deep) 55%,#17407a 100%)}
.screen-login{left:79px}
.screen-weeks{left:353px}
.screen-welcome{left:627px}
.screen-profile{left:900px}
.scene-photo{position:absolute;inset:0;background:radial-gradient(ellipse at 70% 40%,rgba(90,130,210,.35),transparent 60%),radial-gradient(ellipse at 30% 85%,rgba(70,120,80,.25),transparent 55%)}
.heading{font-family:"Titillium Web",sans-serif;font-weight:700;text-align:center;position:absolute;left:0;right:0}
.top-bar{position:absolute;left:0;right:0;top:0;height:25px;background:var(--bar)}
.top-bar svg{position:absolute;top:7px;width:11px;height:11px}
.top-bar .back{left:14px}.top-bar .search{right:14px}
.bottom-nav .chip{position:absolute;top:421px;width:28px;height:28px;border-radius:50%;background:var(--nav-chip);display:flex;align-items:center;justify-content:center;color:var(--ink)}
.bottom-nav .chip svg{width:15px;height:15px}
.c1{left:17px}.c2{left:68px}.c3{left:118px}.c4{left:169px}
/* login */
.brand{position:absolute;top:128px;left:0;right:0;display:flex;align-items:center;justify-content:center;gap:6px;font-family:"Titillium Web",sans-serif;font-weight:700;font-size:17px;letter-spacing:.5px}
.brand-dot{width:12px;height:12px;border-radius:50%;background:var(--white)}
.login-title{top:182px;font-size:16px}
.field{position:absolute;left:17px;width:179px;height:32px;background:var(--white);color:#3a3f4e;font-size:8.5px;padding:0 16px;display:flex;align-items:center}
.f-user{top:221px}.f-pass{top:263px}
.btn-create{position:absolute;left:17px;top:309px;width:179px;height:33px;background:var(--navy);font-family:"Titillium Web",sans-serif;font-weight:700;font-size:11px;display:flex;align-items:center;justify-content:center}
/* weeks */
.weeks-title{top:38px;font-size:12px}
.week{position:absolute;width:45px;height:50px;background:var(--white);border-radius:4px;display:flex;flex-direction:column;align-items:center;justify-content:center;gap:2px}
.week svg{width:24px;height:24px}
.week span{font-family:"Titillium Web",sans-serif;font-weight:700;font-size:9px;color:var(--ink);line-height:1}
/* welcome */
.welcome-title{top:54px;font-size:17px}
.plan{position:absolute;left:16px;top:93px;width:181px}
.plan-head{height:31px;background:var(--navy);font-family:"Titillium Web",sans-serif;font-weight:700;font-size:11px;display:flex;align-items:center;justify-content:center}
.plan-body{background:var(--white);color:var(--ink);padding:12px 17px 14px;font-size:9.5px;line-height:16.5px}
.plan-body b{font-weight:600}
.plan-body p.note{margin-top:5px;line-height:14px}
.ready{top:284px;font-family:"Titillium Web",sans-serif;font-weight:700;font-size:12px;line-height:17px}
.answer{position:absolute;top:327px;width:28px;height:28px;border-radius:50%;display:flex;align-items:center;justify-content:center}
.answer svg{width:14px;height:14px}
.yes{left:75px;background:var(--ok)}.no{left:110px;background:var(--no)}
/* profile */
.profile-title{top:48px;font-size:12px}
.athlete{position:absolute;left:10px;width:192px;height:64px;background:var(--white);color:var(--ink)}
.athlete .photo{position:absolute;left:6px;top:6px;width:67px;height:53px;background:radial-gradient(circle at 20% 30%,#6d7a8c,#1c2433 60%),#1c2433}
.athlete .info{position:absolute;left:82px;top:9px;font-size:7px;line-height:9.6px}
.athlete .info b{font-weight:600}
.athlete .score{position:absolute;left:172px;top:6px;width:11px;height:11px;border-radius:50%;background:var(--bar);color:var(--white);font-size:5px;font-weight:600;display:flex;align-items:center;justify-content:center}
</style>
</head>
<body>
<svg width="0" height="0" style="position:absolute">
  <defs>
    <symbol id="ball" viewBox="0 0 24 24">
      <circle cx="12" cy="12" r="10.5" fill="#fff" stroke="currentColor" stroke-width="1.6"/>
      <polygon points="12,8 15.8,10.8 14.4,15.2 9.6,15.2 8.2,10.8" fill="currentColor"/>
      <path d="M12 1.8v3.4M21.6 9.2l-3.3 1M18.4 20.2l-2-2.8M5.6 20.2l2-2.8M2.4 9.2l3.3 1" stroke="currentColor" stroke-width="1.6"/>
      <path d="M9.4 2.2 12 4l2.6-1.8M22 12.6l-1.4-3.6M15.6 21.6l2.8-1.6M5.6 20.2l2.8 1.4M2 12.6l1.2-3.6" fill="currentColor" stroke="currentColor" stroke-width="1.4"/>
    </symbol>
    <symbol id="i-ball" viewBox="0 0 24 24">
      <circle cx="12" cy="12" r="10" fill="none" stroke="currentColor" stroke-width="2.4"/>
      <polygon points="12,8 15.8,10.8 14.4,15.2 9.6,15.2 8.2,10.8" fill="currentColor"/>
    </symbol>
    <symbol id="i-user" viewBox="0 0 24 24">
      <circle cx="12" cy="7.5" r="5" fill="currentColor"/>
      <path d="M3 22c0-5 4-8 9-8s9 3 9 8z" fill="currentColor"/>
    </symbol>
    <symbol id="i-shield" viewBox="0 0 24 24">
      <path d="M12 2 3.5 5v6c0 5.5 3.7 9.4 8.5 11 4.8-1.6 8.5-5.5 8.5-11V5z" fill="none" stroke="currentColor" stroke-width="2.4"/>
      <path d="M12 4.6v15.2c3.6-1.4 6-4.6 6-8.8V6.6z" fill="currentColor"/>
    </symbol>
    <symbol id="i-boot" viewBox="0 0 24 24">
      <path d="M3 7l4-1 2 4 4 1 7 3c1.5.6 1.5 3 0 3.5L5 18c-1.5.2-2.5-.8-2.5-2z" fill="none" stroke="currentColor" stroke-width="2"/>
      <path d="M6 19.5v2M11 19v2M16 18v2" stroke="currentColor" stroke-width="2"/>
    </symbol>
    <symbol id="i-back" viewBox="0 0 24 24"><path d="M22 12H5M12 3l-9 9 9 9" fill="none" stroke="#fff" stroke-width="3.5"/></symbol>
    <symbol id="i-search" viewBox="0 0 24 24"><circle cx="10" cy="10" r="7" fill="none" stroke="#fff" stroke-width="3.2"/><path d="M15 15l7 7" stroke="#fff" stroke-width="3.5"/></symbol>
  </defs>
</svg>

<!-- Login -->
<section class="screen screen-login">
  <div class="scene-photo" role="img" aria-label="Soccer players in action on a pitch, tinted blue"></div>
  <div class="brand"><span class="brand-dot"></span>KELPMARROW</div>
  <h1 class="heading login-title">ATHLETE LOGIN</h1>
  <div class="field f-user">USERNAME:</div>
  <div class="field f-pass">PASSWORD:</div>
  <div class="btn-create">CREATE ACCOUNT</div>
</section>

<!-- Weekly grid -->
<section class="screen screen-weeks">
  <div class="scene-photo" role="img" aria-label="Soccer players in action on a pitch, tinted blue"></div>
  <div class="top-bar"><svg class="back"><use href="#i-back"/></svg><svg class="search"><use href="#i-search"/></svg></div>
  <h2 class="heading weeks-title">WEEKLY TRAINING CHALLENGE</h2>
  <div class="week" style="left:9px;top:68px;color:#5b5f66"><svg><use href="#ball"/></svg><span>W1</span></div>
  <div class="week" style="left:58px;top:68px;color:#5b5f66"><svg><use href="#ball"/></svg><span>W2</span></div>
  <div class="week" style="left:107px;top:68px;color:#5b5f66"><svg><use href="#ball"/></svg><span>W3</span></div>
  <div class="week" style="left:156px;top:68px;color:#5b5f66"><svg><use href="#ball"/></svg><span>W4</span></div>
  <div class="week" style="left:9px;top:125px;color:#5b5f66"><svg><use href="#ball"/></svg><span>W5</span></div>
  <div class="week" style="left:58px;top:125px;color:#5cb531"><svg><use href="#ball"/></svg><span>W6</span></div>
  <div class="week" style="left:107px;top:125px;color:#ec5a3a"><svg><use href="#ball"/></svg><span>W7</span></div>
  <div class="week" style="left:156px;top:125px;color:#3b2fc9"><svg><use href="#ball"/></svg><span>W8</span></div>
  <div class="week" style="left:9px;top:182px;color:#2b33c8"><svg><use href="#ball"/></svg><span>W9</span></div>
  <div class="week" style="left:58px;top:182px;color:#e07f33"><svg><use href="#ball"/></svg><span>W10</span></div>
  <div class="week" style="left:107px;top:182px;color:#5a3710"><svg><use href="#ball"/></svg><span>W11</span></div>
  <div class="week" style="left:156px;top:182px;color:#3fb1e4"><svg><use href="#ball"/></svg><span>W12</span></div>
  <div class="week" style="left:9px;top:239px;color:#6b3b10"><svg><use href="#ball"/></svg><span>W13</span></div>
  <div class="week" style="left:58px;top:239px;color:#2a9ae8"><svg><use href="#ball"/></svg><span>W14</span></div>
  <div class="week" style="left:107px;top:239px;color:#62b32e"><svg><use href="#ball"/></svg><span>W15</span></div>
  <div class="week" style="left:156px;top:239px;color:#e22530"><svg><use href="#ball"/></svg><span>W16</span></div>
  <div class="week" style="left:9px;top:296px;color:#5b5f66"><svg><use href="#ball"/></svg><span>W17</span></div>
  <div class="week" style="left:58px;top:296px;color:#5b5f66"><svg><use href="#ball"/></svg><span>W18</span></div>
  <div class="week" style="left:107px;top:296px;color:#5b5f66"><svg><use href="#ball"/></svg><span>W19</span></div>
  <div class="week" style="left:156px;top:296px;color:#5b5f66"><svg><use href="#ball"/></svg><span>W20</span></div>
  <div class="week" style="left:9px;top:353px;color:#5b5f66"><svg><use href="#ball"/></svg><span>W21</span></div>
  <div class="week" style="left:58px;top:353px;color:#5b5f66"><svg><use href="#ball"/></svg><span>W22</span></div>
  <div class="week" style="left:107px;top:353px;color:#5b5f66"><svg><use href="#ball"/></svg><span>W23</span></div>
  <div class="week" style="left:156px;top:353px;color:#5b5f66"><svg><use href="#ball"/></svg><span>W24</span></div>
  <nav class="bottom-nav">
    <div class="chip c1"><svg><use href="#i-ball"/></svg></div>
    <div class="chip c2"><svg><use href="#i-user"/></svg></div>
    <div class="chip c3"><svg><use href="#i-shield"/></svg></div>
    <div class="chip c4"><svg><use href="#i-boot"/></svg></div>
  </nav>
</section>

<!-- Welcome -->
<section class="screen screen-welcome">
  <div class="scene-photo" role="img" aria-label="Soccer players in action on a pitch, tinted blue"></div>
  <div class="top-bar"><svg class="back"><use href="#i-back"/></svg><svg class="search"><use href="#i-search"/></svg></div>
  <h2 class="heading welcome-title">WELCOME</h2>
  <div class="plan">
    <div class="plan-head">Week 7 Training</div>
    <div class="plan-body">
      <p><b>Technical</b></p>
      <p><b>Radar:</b> First Touch</p>
      <p><b>Equipment:</b> 1 ball, 10 cones</p>
      <p><b>Space:</b> 20 meters</p>
      <p class="note">If you don’t have equipment or space - you need a soccer ball &amp; desire to improve</p>
    </div>
  </div>
  <p class="heading ready">Are YOU Ready<br>for the Weekly Challenge?</p>
  <div class="answer yes"><svg viewBox="0 0 24 24"><path d="M3 12.5l6 6L21 6" fill="none" stroke="#fff" stroke-width="4"/></svg></div>
  <div class="answer no"><svg viewBox="0 0 24 24"><path d="M4 4l16 16M20 4 4 20" fill="none" stroke="#fff" stroke-width="4"/></svg></div>
  <nav class="bottom-nav">
    <div class="chip c1"><svg><use href="#i-ball"/></svg></div>
    <div class="chip c2"><svg><use href="#i-user"/></svg></div>
    <div class="chip c3"><svg><use href="#i-shield"/></svg></div>
    <div class="chip c4"><svg><use href="#i-boot"/></svg></div>
  </nav>
</section>

<!-- Profile -->
<section class="screen screen-profile">
  <div class="scene-photo" role="img" aria-label="Soccer players in action on a pitch, tinted blue"></div>
  <div class="top-bar"><svg class="back"><use href="#i-back"/></svg><svg class="search"><use href="#i-search"/></svg></div>
  <h2 class="heading profile-title">PROFILE</h2>
  <article class="athlete" style="top:81px"><div class="photo" role="img" aria-label="Athlete portrait in blue kit under stadium lights"></div><div class="info"><b>#AZ12345</b><br>Dario Venn<br>18 / M / 6’2 / 200<br>Primary Position: 7<br>Secondary Position: 5</div><div class="score">82</div></article>
  <article class="athlete" style="top:155px"><div class="photo" role="img" aria-label="Athlete portrait in blue kit under stadium lights"></div><div class="info"><b>#AZ12345</b><br>Dario Venn<br>18 / M / 6’2 / 200<br>Primary Position: 7<br>Secondary Position: 5</div><div class="score">82</div></article>
  <article class="athlete" style="top:228px"><div class="photo" role="img" aria-label="Athlete portrait in blue kit under stadium lights"></div><div class="info"><b>#AZ12345</b><br>Dario Venn<br>18 / M / 6’2 / 200<br>Primary Position: 7<br>Secondary Position: 5</div><div class="score">82</div></article>
  <article class="athlete" style="top:302px"><div class="photo" role="img" aria-label="Athlete portrait in blue kit under stadium lights"></div><div class="info"><b>#AZ12345</b><br>Dario Venn<br>18 / M / 6’2 / 200<br>Primary Position: 7<br>Secondary Position: 5</div><div class="score">82</div></article>
  <nav class="bottom-nav">
    <div class="chip c1"><svg><use href="#i-ball"/></svg></div>
    <div class="chip c2"><svg><use href="#i-user"/></svg></div>
    <div class="chip c3"><svg><use href="#i-shield"/></svg></div>
    <div class="chip c4"><svg><use href="#i-boot"/></svg></div>
  </nav>
</section>
</body>
</html>
```